Accounting Business needs double sided DL flyer design

We need a double sided DL flyer designed,
Front side with logo, web address and our short intro.
Backside to have a list of services.
Our colours are blue and a concrete grey colour. Look at our website for a feel for our colour scheme.
www.lanternwellgroup.com.au
I have included the pic from our website to possibly use but we are also open to new creative ideas.
Target Market(s)
Our target market are proactive business owners, particularly in the wine and hospitality industry.
Industry/Entity Type
Business
Look and feel

```html
<!DOCTYPE html>
<html lang="en">
<head>
<meta charset="utf-8">
<title>Lanternwell Group – DL Flyer</title>
<link href="https://fonts.googleapis.com/css2?family=Roboto:wght@400;500;700;900&family=Exo+2:wght@500;600;700;800&family=Lato:ital,wght@1,400;1,700&display=swap" rel="stylesheet">
<style>
  :root{
    --navy:#1c3f7a;
    --blue:#2a5ca8;
    --sky:#3a7cc4;
    --ink:#3a3d42;
    --grey:#6b6f75;
    --concrete:#b8bcc0;
    --paper:#f2f5fa;
    --stage:#e6e7e9;
  }
  *{margin:0;padding:0;box-sizing:border-box}
  html,body{width:1200px;height:902px;overflow:hidden;background:var(--stage)}
  .stage{position:relative;width:1200px;height:902px}
  .flyer{position:absolute;width:380px;height:781px;overflow:hidden;
    background:linear-gradient(180deg,#ffffff 0%,var(--paper) 60%,#e4eaf3 100%);
    box-shadow:0 6px 18px rgba(0,0,0,.25)}
  .flyer--front{left:138px;top:31px}
  .flyer--back{left:637px;top:62px}

  .brand{position:absolute;font-family:"Exo 2",sans-serif;font-weight:700;color:var(--navy);
    display:flex;align-items:center;gap:8px;letter-spacing:.5px}
  .brand__mark{width:26px;height:26px;border-radius:50%;background:var(--navy);flex:none}
  .brand__text{display:flex;flex-direction:column;line-height:1}
  .brand__name{font-size:17px}
  .brand__tag{font-size:7px;letter-spacing:1.4px;margin-top:4px;font-weight:600}

  /* front */
  .front-band{position:absolute;left:0;top:0;width:380px;height:375px}
  .front-photo{position:absolute;left:0;top:52px;width:356px;height:302px;
    border-radius:0 120px 120px 0;border:5px solid #fff;border-left:none;
    background:linear-gradient(160deg,#d9dadb 0%,#c4c6c8 45%,#9b9ea2 75%,#7d8085 100%)}
  .front .brand{left:28px;top:92px}
  .headline{position:absolute;left:22px;top:415px;width:338px;height:190px;font-family:Roboto,sans-serif;color:var(--ink)}
  .headline__a{position:absolute;left:0;top:-8px;font-size:160px;font-weight:900;color:var(--navy);line-height:1}
  .headline__line{position:absolute;right:0;white-space:nowrap;font-weight:500;line-height:1}
  .headline__line--1{top:14px;font-size:33px}
  .headline__line--2{top:55px;font-size:25px}
  .headline__line--3{top:92px;font-size:18px}
  .headline__success{position:absolute;left:0;right:0;top:124px;white-space:nowrap;font-size:49px;font-weight:700;color:var(--sky);letter-spacing:.5px;text-align:right}

  /* contact band */
  .contact{position:absolute;left:0;bottom:0;width:380px;height:130px;text-align:center;color:#fff}
  .contact__band{position:absolute;left:0;top:0}
  .contact__label{position:relative;padding-top:16px;font-family:"Exo 2",sans-serif;font-weight:600;font-size:20px;line-height:1.2}
  .contact__phone{position:relative;margin-top:2px;font-family:"Exo 2",sans-serif;font-weight:800;font-size:38px;line-height:1.1;letter-spacing:1px;
    display:flex;justify-content:center;align-items:center;gap:6px}
  .contact__icon{flex:none}
  .contact__web{position:relative;margin:8px auto 0;width:256px;padding:5px 0;font-family:Roboto,sans-serif;font-size:13px;
    border-top:1px solid rgba(255,255,255,.35);border-bottom:2px solid var(--sky);display:flex;justify-content:center;align-items:center;gap:6px}

  /* back */
  .back-photo{position:absolute;left:0;top:0;width:380px;height:200px}
  .bubbles{position:absolute;left:0;top:176px;width:380px;height:115px}
  .bubble{position:absolute;top:0;width:112px;height:112px;border-radius:50%;border:4px solid #fff;
    box-shadow:0 0 0 2px var(--navy),0 3px 6px rgba(0,0,0,.3)}
  .bubble--1{left:22px;background:linear-gradient(140deg,#dfe9f4,#8fb4d8)}
  .bubble--2{left:137px;background:linear-gradient(140deg,#e9eef2,#a9b3bd)}
  .bubble--3{left:252px;background:linear-gradient(140deg,#c9cdd2,#4b4f56)}
  .services-title{position:absolute;left:83px;top:304px;width:224px;height:34px;border-radius:17px;
    background:linear-gradient(180deg,#2f66b3,var(--navy));border:2px solid #fff;box-shadow:0 0 0 1px var(--navy),0 2px 4px rgba(0,0,0,.3);
    color:#fff;font-family:Roboto,sans-serif;font-weight:500;font-size:21px;text-align:center;line-height:30px}
  .services{position:absolute;top:358px;list-style:none;font-family:Lato,sans-serif;font-style:italic;font-size:12.5px;color:var(--ink);line-height:1.25}
  .services--left{left:22px;width:190px}
  .services--right{left:222px;width:160px}
  .service{display:flex;align-items:center;gap:10px;margin-bottom:13px;min-height:26px}
  .service__icon{flex:none;width:26px;height:26px;border-radius:50%;background:#44474c;border:2px solid #c8ccd1;
    display:flex;align-items:center;justify-content:center}
  .service__icon::after{content:"";width:9px;height:9px;border:1.5px solid #fff;border-radius:2px}
  .back .brand{left:176px;top:617px}
  .back .brand__name{font-size:14px}
  .back .brand__tag{font-size:6px}
  .back .brand__mark{width:22px;height:22px}
</style>
</head>
<body>
<main class="stage">

  <section class="flyer flyer--front front" aria-label="Flyer front">
    <svg class="front-band" viewBox="0 0 380 375" aria-hidden="true">
      <defs>
        <linearGradient id="bandFill" x1="0" y1="0" x2="0" y2="1">
          <stop offset="0" stop-color="#1f4b8f"/><stop offset=".6" stop-color="#3470b8"/><stop offset="1" stop-color="#f2f5fa" stop-opacity="0"/>
        </linearGradient>
      </defs>
      <path d="M0 0H380V300Q380 360 320 368H0Z" fill="url(#bandFill)"/>
    </svg>
    <div class="front-photo" role="img" aria-label="Photo of white concrete stairs rising along a grey concrete wall"></div>
    <div class="brand">
      <span class="brand__mark"></span>
      <span class="brand__text"><span class="brand__name">LANTERNWELL GROUP</span><span class="brand__tag">BUSINESS ADVISORS &amp; ACCOUNTANTS</span></span>
    </div>

    <h1 class="headline">
      <span class="headline__a">A</span>
      <span class="headline__line headline__line--1">GUIDING HAND</span>
      <span class="headline__line headline__line--2">VOICE OF REASON</span>
      <span class="headline__line headline__line--3">TRUE SOUNDING BOARD</span>
      <span class="headline__success">FOR SUCCESS</span>
    </h1>

    <footer class="contact">
      <svg class="contact__band" width="380" height="130" viewBox="0 0 380 130" aria-hidden="true">
        <defs>
          <linearGradient id="footFillA" x1="0" y1="0" x2="0" y2="1">
            <stop offset="0" stop-color="#6a6c70"/><stop offset=".5" stop-color="#3d3f43"/><stop offset="1" stop-color="#6a6c70"/>
          </linearGradient>
        </defs>
        <path d="M0 18Q190 -12 380 18V130H0Z" fill="url(#footFillA)"/>
        <path d="M0 14Q190 -16 380 14" fill="none" stroke="#1c3f7a" stroke-width="4"/>
      </svg>
      <p class="contact__label">Contact Us</p>
      <p class="contact__phone">
        <svg class="contact__icon" width="24" height="24" viewBox="0 0 24 24" aria-hidden="true"><circle cx="12" cy="12" r="10.5" fill="none" stroke="#fff" stroke-width="1.6"/><path d="M8.5 6.5l2 2-1.2 1.6c.8 1.7 2 2.9 3.6 3.7l1.6-1.2 2 2-1.4 1.8c-3.6-.4-7.7-4.5-8.1-8.1z" fill="#fff"/></svg>
        <span>0491 570 110</span>
      </p>
      <p class="contact__web">
        <svg class="contact__icon" width="11" height="11" viewBox="0 0 12 12" aria-hidden="true"><circle cx="6" cy="6" r="5" fill="none" stroke="#fff"/><path d="M1 6h10M6 1c-2 3-2 7 0 10M6 1c2 3 2 7 0 10" fill="none" stroke="#fff" stroke-width=".8"/></svg>
        <span>www.lanternwellgroup.com.au</span>
      </p>
    </footer>
  </section>

  <section class="flyer flyer--back back" aria-label="Flyer back">
    <svg class="back-photo" viewBox="0 0 380 200" role="img" aria-label="Photo of hands working with a calculator, laptop and financial charts on a desk">
      <defs>
        <linearGradient id="deskFill" x1="0" y1="0" x2="1" y2="1">
          <stop offset="0" stop-color="#dfe6ee"/><stop offset=".5" stop-color="#b7c6d6"/><stop offset="1" stop-color="#8795a5"/>
        </linearGradient>
      </defs>
      <path d="M0 0H380V110Q330 190 200 182H0Z" fill="url(#deskFill)"/>
      <path d="M380 110Q330 190 200 182" fill="none" stroke="#fff" stroke-width="4"/>
    </svg>
    <div class="bubbles">
      <div class="bubble bubble--1" role="img" aria-label="Photo of a hand using a tablet showing charts"></div>
      <div class="bubble bubble--2" role="img" aria-label="Photo of a tablet on colourful financial reports"></div>
      <div class="bubble bubble--3" role="img" aria-label="Photo of business people joining hands"></div>
    </div>

    <h2 class="services-title">OUR SERVICES</h2>

    <ul class="services services--left">
      <li class="service"><span class="service__icon"></span>Taxation Compliance</li>
      <li class="service"><span class="service__icon"></span>Financial &amp; Management Reporting</li>
      <li class="service"><span class="service__icon"></span>Self-Managed Superannuation</li>
      <li class="service"><span class="service__icon"></span>Virtual CFO</li>
      <li class="service"><span class="service__icon"></span>Business Planning</li>
      <li class="service"><span class="service__icon"></span>KPIs &amp; Performance Monitoring</li>
    </ul>
    <ul class="services services--right">
      <li class="service"><span class="service__icon"></span>Succession Planning</li>
      <li class="service"><span class="service__icon"></span>Estate Planning</li>
      <li class="service"><span class="service__icon"></span>Cloud Solutions</li>
      <li class="service"><span class="service__icon"></span>Business Support Services</li>
      <li class="service"><span class="service__icon"></span>The Wine Industry</li>
    </ul>

    <div class="brand">
      <span class="brand__mark"></span>
      <span class="brand__text"><span class="brand__name">LANTERNWELL GROUP</span><span class="brand__tag">BUSINESS ADVISORS &amp; ACCOUNTANTS</span></span>
    </div>

    <footer class="contact">
      <svg class="contact__band" width="380" height="130" viewBox="0 0 380 130" aria-hidden="true">
        <defs>
          <linearGradient id="footFillB" x1="0" y1="0" x2="0" y2="1">
            <stop offset="0" stop-color="#6a6c70"/><stop offset=".5" stop-color="#3d3f43"/><stop offset="1" stop-color="#6a6c70"/>
          </linearGradient>
        </defs>
        <path d="M0 18Q190 -12 380 18V130H0Z" fill="url(#footFillB)"/>
        <path d="M0 14Q190 -16 380 14" fill="none" stroke="#1c3f7a" stroke-width="4"/>
      </svg>
      <p class="contact__label">Contact Us</p>
      <p class="contact__phone">
        <svg class="contact__icon" width="24" height="24" viewBox="0 0 24 24" aria-hidden="true"><circle cx="12" cy="12" r="10.5" fill="none" stroke="#fff" stroke-width="1.6"/><path d="M8.5 6.5l2 2-1.2 1.6c.8 1.7 2 2.9 3.6 3.7l1.6-1.2 2 2-1.4 1.8c-3.6-.4-7.7-4.5-8.1-8.1z" fill="#fff"/></svg>
        <span>0491 570 110</span>
      </p>
      <p class="contact__web">
        <svg class="contact__icon" width="11" height="11" viewBox="0 0 12 12" aria-hidden="true"><circle cx="6" cy="6" r="5" fill="none" stroke="#fff"/><path d="M1 6h10M6 1c-2 3-2 7 0 10M6 1c2 3 2 7 0 10" fill="none" stroke="#fff" stroke-width=".8"/></svg>
        <span>www.lanternwellgroup.com.au</span>
      </p>
    </footer>
  </section>

</main>
</body>
</html>
```